Classy business card for accounting firm

We're looking for a new business card for our accounting firm. Our logo was designed by Brandolith, so all of the design info we would like to use has been provided. The specific font provided isn't required to be used.

We want the card to look classy and elegent. Probably more minimalistic, but still with some pops of color.

The options we would like to include on the card are as follows:
1. Main office phone line
2. Direct phone line
3. Email address
4. Website URL
5. Name
6. Title (CEO, President, etc.)
7. Firm Address

The design and card should be double sided!!! The drop down box in the project brief for some reason is defaulting to single sided. Not sure why this is happening.

Thanks!

Contact Information for Business Card

The options we would like to include on the card are as follows: 1. Main office phone line 2. Direct phone line 3. Email address 4. Website URL 5. Name 6. Title (CEO, President, etc.) 7. Firm Address

Requirements
Must have
• Card must be double sided.

```html
<!DOCTYPE html>
<html lang="en">
<head>
<meta charset="utf-8">
<title>Ledgerwell Partners – Business Card</title>
<link rel="stylesheet" href="https://fonts.googleapis.com/css2?family=Montserrat:wght@400;500;600;700&display=swap">
<style>
  :root {
    --orange: #f47c20;
    --green: #b5c231;
    --ink: #1e1e1e;
    --grey: #4a4a4a;
    --paper: #ffffff;
    --backdrop: #d9d9d9;
  }
  * { box-sizing: border-box; margin: 0; padding: 0; }
  html, body { width: 1200px; height: 856px; overflow: hidden; }
  body {
    background: var(--backdrop);
    font-family: "Montserrat", sans-serif;
    display: flex; align-items: center; justify-content: center; gap: 40px;
  }
  .card {
    position: relative; width: 540px; height: 309px; overflow: hidden;
    box-shadow: 0 10px 30px rgba(0,0,0,.25);
  }
  /* Front */
  .card-front { background: var(--paper); color: var(--ink); }
  .front-band { position: absolute; left: 0; bottom: 0; width: 100%; height: 40px; }
  .front-body { position: absolute; inset: 46px 30px 60px 34px; display: flex; flex-direction: column; }
  .brand { display: flex; align-items: center; gap: 12px; }
  .brand-mark { width: 26px; height: 26px; background: var(--orange); flex: none; }
  .brand-name { font-weight: 500; font-size: 21px; letter-spacing: 2px; color: var(--grey); }
  .tagline { display: flex; align-items: center; gap: 8px; margin: 6px 0 0 38px; }
  .tagline span { font-size: 8.5px; letter-spacing: 2.2px; color: var(--grey); }
  .tagline i { height: 1px; width: 60px; background: var(--green); display: block; }
  .details { display: flex; margin-top: 28px; }
  .person { width: 210px; padding-right: 18px; border-right: 1.5px solid var(--green); }
  .person-name { font-weight: 700; font-size: 19px; letter-spacing: .5px; }
  .person-name .first { color: var(--green); }
  .person-name .last { color: var(--orange); }
  .person-title { font-size: 12px; margin-top: 4px; }
  .address { font-size: 11.5px; line-height: 1.45; margin-top: 8px; }
  .contacts { list-style: none; padding-left: 18px; display: flex; flex-direction: column; gap: 7px; }
  .contacts li { display: flex; align-items: center; gap: 9px; font-size: 12px; }
  .contacts svg { width: 14px; height: 14px; flex: none; }
  /* Back */
  .card-back { background: var(--orange); color: var(--paper); display: flex; flex-direction: column; align-items: center; justify-content: center; }
  .back-mark { width: 58px; height: 58px; background: var(--paper); margin-bottom: 22px; }
  .back-name { font-weight: 600; font-size: 30px; letter-spacing: 3px; }
  .back-tagline { display: flex; align-items: center; gap: 12px; margin-top: 8px; }
  .back-tagline span { font-size: 11px; letter-spacing: 3px; font-weight: 500; }
  .back-tagline i { display: block; width: 80px; height: 1.5px; background: var(--paper); }
</style>
</head>
<body>
  <section class="card card-front" aria-label="Business card front">
    <div class="front-body">
      <div class="brand">
        <span class="brand-mark"></span>
        <span class="brand-name">LEDGERWELL PARTNERS</span>
      </div>
      <div class="tagline"><i></i><span>SOLVING TAX PROBLEMS</span><i></i></div>
      <div class="details">
        <div class="person">
          <p class="person-name"><span class="first">DANIEL</span> <span class="last">HARROW</span></p>
          <p class="person-title">CEO, President</p>
          <p class="address">Meridian Court 1820 Elm<br>Ridgefield Lane Suite 310</p>
        </div>
        <ul class="contacts">
          <li><svg viewBox="0 0 16 16"><path fill="var(--green)" d="M3 2h3l1 4-2 1a9 9 0 0 0 4 4l1-2 4 1v3a1 1 0 0 1-1 1A12 12 0 0 1 2 3a1 1 0 0 1 1-1z"/></svg>555-201-3348</li>
          <li><svg viewBox="0 0 16 16"><rect x="4" y="1" width="8" height="14" rx="1.5" fill="none" stroke="var(--green)" stroke-width="1.6"/><circle cx="8" cy="12.5" r=".9" fill="var(--green)"/></svg>555-476-1290</li>
          <li><svg viewBox="0 0 16 16"><rect x="1" y="3" width="14" height="10" fill="var(--green)"/><path d="M1 3l7 6 7-6" fill="none" stroke="#fff" stroke-width="1.2"/></svg>info@ledgerwellpartners.com</li>
          <li><svg viewBox="0 0 16 16"><circle cx="8" cy="8" r="6.5" fill="var(--green)"/><path d="M1.5 8h13M8 1.5c-3 3.5-3 9.5 0 13M8 1.5c3 3.5 3 9.5 0 13" fill="none" stroke="#fff" stroke-width=".9"/></svg>www.ledgerwellpartners.com</li>
        </ul>
      </div>
    </div>
    <svg class="front-band" viewBox="0 0 540 40" preserveAspectRatio="none" aria-hidden="true">
      <polygon points="0,40 0,22 330,22 336,40" fill="var(--orange)"/>
      <polygon points="340,40 334,22 352,0 540,0 540,40" fill="var(--green)"/>
      <polygon points="336,40 330,22 334,22 340,40" fill="#fff"/>
    </svg>
  </section>

  <section class="card card-back" aria-label="Business card back">
    <span class="back-mark"></span>
    <p class="back-name">LEDGERWELL PARTNERS</p>
    <div class="back-tagline"><i></i><span>SOLVING TAX PROBLEMS</span><i></i></div>
  </section>
</body>
</html>
```